Website for premium health insurance and concierge medicine

This is a brand new website for Vantor Insurance Services that specializes in Health Insurance and Concierge Medicine for high net-worth and affluent individuals and families. Through this website, clients will be able to learn about products and services, submit applications, and complete self enrollment forms. The website needs to have a premium look & feel that will appeal to a discerning high net-worth individual.

I’m looking for 4 pages in total to begin with. I’m also looking for a designer who will be interested in continuing to build out this new site further over the next few months.

The headline for each page is listed below:

Page 1: HOME PAGE
“Premium Healthcare | Bespoke Concierge Services | Absolute Peace of Mind.”

Page 2: HEALTH INSURANCE
“Premium Healthcare | Elevated.”

Page 3: CONCIERGE MEDICINE
“Personalized Medicine | At-Home Concierge Care | Your Private Physician, 24/7.”

Page 4: DENTAL & VISION
“Your Smile | Your Vision | Perfected.”

Here are several links to existing websites that can be used as design inspiration:

https://brevanwell.com
https://www.quemby.org/specialties-services/other-programs-services/concierge-medicine
https://physelmdkx.com

More generally speaking, I like a clean, modern, dutch style of websites. Here’s an unrelated site that has a good design:

https://www.ostravine.com

Here are a few additional phrases and keywords that will help inspire the design:

Premium Health Insurance
Executive Health Insurance
Concierge Medicine
24/7 access dedicated concierge team
Integrative Concierge Care

I will upload logo files below, here are the font & colors information:

Font: Trajan Pro Bold
Colors:
Blue: hex code: 0071BD, Rgb code: 0, 113, 189  cmyk code: 87,53,0,0
Gray: hex code: #666666, Rgb code: 102,102,102 cmyk code: 60,51,51,20

```html
<!DOCTYPE html>
<html lang="en">
<head>
<meta charset="utf-8">
<title>Vantor Insurance Services — Premium Health Insurance &amp; Concierge Medicine</title>
<link href="https://fonts.googleapis.com/css2?family=Cormorant+Garamond:wght@400;500;600&family=Lato:wght@300;400;700&display=swap" rel="stylesheet">
<style>
:root{
  --blue:#0071bd;
  --blue-dark:#00579a;
  --gray:#666666;
  --ink:#222831;
  --muted:#8a8f96;
  --line:#d9dde2;
  --white:#ffffff;
  --paper:#f7f9fb;
  --dark:#2a2c30;
  --darker:#1f2023;
  --sky:#e6eef5;
  --photo-light:#dfe6ec;
  --photo-mid:#b9c6d1;
}
*{margin:0;padding:0;box-sizing:border-box}
html,body{width:1200px;height:4164px;overflow:hidden}
body{font-family:'Lato',Arial,sans-serif;color:var(--gray);background:var(--white);position:relative}
.serif{font-family:'Cormorant Garamond',Georgia,serif}
.photo{display:block}
.brand{display:flex;align-items:center;gap:10px;font-family:'Lato',Arial,sans-serif;font-weight:700;color:var(--blue);letter-spacing:.04em}
.brand-mark{width:34px;height:34px;border-radius:50%;background:var(--blue);flex:none}

/* hero */
.hero{position:absolute;left:0;top:0;width:1200px;height:620px}
.hero-side{position:absolute;left:0;top:0;width:330px;height:620px;padding:24px 28px 0 40px}
.hero-side .brand{font-size:15px;margin-bottom:110px}
.hero-side .brand-mark{width:64px;height:64px}
.pillar{margin-bottom:24px}
.pillar h3{font-family:'Cormorant Garamond',Georgia,serif;font-size:20px;font-weight:600;color:var(--ink);margin-bottom:6px}
.pillar p{font-size:10.5px;line-height:1.5;color:var(--gray)}
.btn-outline{display:inline-block;margin-top:12px;width:250px;padding:11px 0;text-align:center;border:1px solid var(--blue);border-radius:3px;color:var(--ink);font-size:14px}
.hero-photo{position:absolute;left:340px;top:0;width:860px;height:620px;background:linear-gradient(110deg,#f2f5f7 0%,#dfe7ec 45%,#c3d0da 100%)}
.nav{position:absolute;right:40px;top:22px;display:flex;gap:34px;align-items:center;font-size:12px;color:var(--ink)}
.nav .login{background:var(--blue);color:var(--white);padding:6px 16px;border-radius:3px}

/* intro */
.intro{position:absolute;top:660px;left:0;width:1200px;text-align:center}
.intro h1{font-weight:300;font-size:31px;line-height:1.35;color:var(--ink);width:960px;margin:0 auto}

/* explore */
.explore{position:absolute;top:1020px;left:0;width:1200px;height:300px}
.explore-photo{position:absolute;left:160px;top:0;width:480px;height:185px;background:linear-gradient(120deg,#eef1f3,#c9d3da)}
.explore-copy{position:absolute;left:672px;top:10px;width:420px}
.explore-copy h2{font-family:'Cormorant Garamond',Georgia,serif;font-weight:500;font-size:27px;color:var(--ink);margin-bottom:12px}
.explore-copy p{font-size:10.5px;line-height:1.6;margin-bottom:48px}
.rule{height:1px;background:var(--line);margin:-30px 0 26px}

/* values */
.values{position:absolute;top:1360px;left:0;width:1200px;height:620px;background:linear-gradient(180deg,var(--darker),var(--dark))}
.value{position:absolute;top:20px;width:345px;color:var(--white)}
.value h3{font-family:'Cormorant Garamond',Georgia,serif;font-weight:500;font-size:24px;margin-bottom:14px}
.value p{font-size:10.5px;line-height:1.55;color:#c9cdd2;height:60px}
.value .photo{margin-top:52px;width:345px;height:340px;border-radius:6px}

/* glance */
.glance{position:absolute;top:1980px;left:0;width:1200px;height:780px;background:linear-gradient(90deg,#f5f8fb 0%,#e3ecf3 55%,#cfdde8 100%)}
.glance h2{position:absolute;left:48px;top:28px;font-family:'Cormorant Garamond',Georgia,serif;font-weight:500;font-size:40px;color:var(--ink)}
.glance-list{position:absolute;left:48px;top:120px;width:560px}
.service{margin-bottom:26px}
.service h3{font-family:'Cormorant Garamond',Georgia,serif;font-weight:600;font-size:24px;color:var(--ink)}
.service .sub{font-size:10px;color:var(--muted);margin:2px 0 10px}
.service p{font-size:10.5px;line-height:1.6}
.glance-photo{position:absolute;right:0;top:0;width:520px;height:780px;background:radial-gradient(circle at 60% 40%,#f3f5f6 0%,#cbd6df 60%,#b6c5d1 100%)}

/* testimonials */
.trust{position:absolute;top:2760px;left:0;width:1200px;height:480px;background:var(--white)}
.trust .brand{position:absolute;top:10px;font-size:15px}
.trust .brand-mark{width:56px;height:56px}
.trust h2{position:absolute;top:22px;left:0;width:1200px;text-align:center;font-family:'Cormorant Garamond',Georgia,serif;font-weight:500;font-size:36px;color:var(--ink)}
.trust .lead{position:absolute;top:80px;left:300px;width:600px;text-align:center;font-size:14px;line-height:1.55;color:var(--gray)}
.cards{position:absolute;top:195px;left:-70px;display:flex;gap:26px}
.card{width:160px;height:220px;padding:14px 12px;border:1px solid var(--line);border-radius:6px;background:var(--white);box-shadow:0 4px 12px rgba(0,0,0,.06)}
.card-head{display:flex;align-items:center;gap:8px;margin-bottom:14px}
.avatar{width:30px;height:30px;border-radius:50%;background:var(--photo-mid);flex:none}
.card-head b{display:block;font-size:11px;color:var(--ink)}
.card-head span{font-size:8px;color:var(--muted)}
.card h4{font-size:11px;color:var(--ink);margin-bottom:8px}
.card p{font-size:8.5px;line-height:1.55}

/* consult */
.consult{position:absolute;top:3320px;left:0;width:1200px;height:460px}
.consult-photo{position:absolute;left:60px;top:0;width:380px;height:440px;background:linear-gradient(180deg,#ffffff,#e9eef2 70%,#d5dde4)}
.consult-copy{position:absolute;left:570px;top:90px;width:440px}
.consult-copy h2{font-family:'Cormorant Garamond',Georgia,serif;font-weight:500;font-size:36px;color:var(--ink)}
.consult-copy .sub{font-size:16px;color:var(--ink);margin:4px 0 18px}
.consult-copy p{font-size:10.5px;line-height:1.6;margin-bottom:18px}
.btn{display:inline-block;background:var(--blue);color:var(--white);font-size:11px;padding:10px 34px;border-radius:3px}

/* footer */
.footer{position:absolute;top:3900px;left:0;width:1200px;height:264px;background:var(--darker);color:#b8bcc2}
.footer .brand{position:absolute;left:60px;top:36px;color:var(--white);font-size:15px}
.footer .brand-mark{width:70px;height:70px;background:var(--white)}
.fcol{position:absolute;top:40px;font-size:9.5px;line-height:2}
.fcol h5{color:var(--white);font-size:10px;font-weight:700;margin-bottom:2px}
.copy{position:absolute;left:420px;top:210px;font-size:9px;color:#8f949a}
</style>
</head>
<body>

<section class="hero">
  <div class="hero-side">
    <div class="brand"><span class="brand-mark"></span>Vantor Insurance Services</div>
    <div class="pillar">
      <h3>Premium Healthcare</h3>
      <p>Vantor offers a curated selection of health coverage designed for discerning individuals and families, giving access to world-class medical institutions, private specialists and personalised care.</p>
    </div>
    <div class="pillar">
      <h3>Bespoke Concierge Service</h3>
      <p>Your health care never runs on a clock. Access your dedicated concierge team 24/7 for appointments, referrals, travel arrangements and every detail of your care.</p>
    </div>
    <div class="pillar">
      <h3>Absolute Peace of Mind</h3>
      <p>Discretion, security and continuity are at the heart of our service. We protect your privacy and your family so that every decision about your health feels certain.</p>
    </div>
    <a class="btn-outline">Get Started</a>
  </div>
  <div class="hero-photo photo" role="img" aria-label="Physician in a white coat standing in a bright modern clinic"></div>
  <nav class="nav">
    <span>Health Insurance</span><span>Concierge Medicine</span><span>Dental &amp; Vision</span><span class="login">Login</span>
  </nav>
</section>

<section class="intro">
  <h1>Tailored insurance solutions and concierge medical care designed exclusively for discerning individuals and families who demand the very best</h1>
</section>

<section class="explore">
  <div class="explore-photo photo" role="img" aria-label="Doctor consulting with a patient across a desk"></div>
  <div class="explore-copy">
    <h2>Explore Our Services</h2>
    <p>Discover a world of elevated healthcare solutions designed for those who expect nothing but the best. From elite health insurance plans to personalized concierge medicine, we offer seamless access to top-tier medical care, private specialists and 24/7 wellness services tailored to your lifestyle.</p>
    <div class="rule"></div>
    <h2>Request a Private Consultation</h2>
    <p>Your health deserves personalized attention. Schedule a discreet, one-on-one consultation with our expert advisors to design a coverage plan tailored to your needs. Whether you seek global health insurance, 24/7 concierge medical care or private medical services, we ensure an exceptional, seamless experience from the very first conversation.</p>
  </div>
</section>

<section class="values">
  <div class="value" style="left:48px">
    <h3>Exclusivity</h3>
    <p>Access world-class medical professionals and premier insurance plans tailored to your lifestyle.</p>
    <div class="photo" style="background:linear-gradient(150deg,#e7ecef,#aebdc8)" role="img" aria-label="Senior doctor speaking with a patient"></div>
  </div>
  <div class="value" style="left:428px">
    <h3>Personalized Service</h3>
    <p>Concierge healthcare at your fingertips: dedicated 24/7 access to private doctors, specialists and wellness experts.</p>
    <div class="photo" style="background:linear-gradient(150deg,#f1efe9,#c7c0b3)" role="img" aria-label="Physician visiting a family at home"></div>
  </div>
  <div class="value" style="left:808px">
    <h3>Absolute Privacy</h3>
    <p>Secure, discreet and designed for high net-worth individuals ensuring your well-being is always the top priority.</p>
    <div class="photo" style="background:linear-gradient(150deg,#e9eef2,#b6c8d6)" role="img" aria-label="Nurse caring for an elderly patient in a clinic"></div>
  </div>
</section>

<section class="glance">
  <h2>Our Service at a Glance</h2>
  <div class="glance-list">
    <div class="service">
      <h3>Health Insurance</h3>
      <div class="sub">Exclusive Plans with Global Coverage</div>
      <p>Gain access to world-class healthcare anywhere in the world. Our personalized health insurance plans provide private hospital rooms, top-tier specialists and international coverage, with dedicated concierge support for complete peace of mind. Tailored solutions protect you and your family, wherever life takes you, with no compromise on quality or privacy.</p>
    </div>
    <div class="service">
      <h3>Concierge Medicine</h3>
      <div class="sub">Private Doctors, 24/7 Access and At-Home Care</div>
      <p>Experience luxury healthcare on your own schedule. With our concierge medicine service, you receive unlimited access to private physicians, same-day appointments and at-home consultations. Whether at home, in your office or traveling, your personal doctor is always available to you.</p>
    </div>
    <div class="service">
      <h3>Dental &amp; Vision</h3>
      <div class="sub">Elite Coverage for a Healthier Smile and Crystal-Clear Vision</div>
      <p>Your smile and vision deserve the highest level of care. Our premium dental and vision plans cover cosmetic and restorative treatments, leading specialists and designer eyewear, giving your family complete, effortless care that reflects the standard you expect.</p>
    </div>
  </div>
  <div class="glance-photo photo" role="img" aria-label="Smiling physician with a stethoscope in a bright corridor"></div>
</section>

<section class="trust">
  <div class="brand" style="left:60px"><span class="brand-mark"></span>Vantor Insurance<br>Services</div>
  <h2>Trusted by Those Who Expect the Best</h2>
  <p class="lead">Our clients demand exceptional healthcare, absolute discretion, and seamless service—and we deliver. Here’s what they have to say about their experience with Vantor Insurance.</p>
  <div class="brand" style="right:40px"><span class="brand-mark"></span>Vantor Insurance<br>Services</div>
  <div class="cards">
    <div class="card"><div class="card-head"><span class="avatar" role="img" aria-label="Client portrait"></span><div><b>Elena Marsh</b><span>Private Client</span></div></div><h4>“You guys nailed it!”</h4><p>The team arranged every detail of our family plan with care. Every call was answered quickly and we always felt looked after. Truly a premium service.</p></div>
    <div class="card"><div class="card-head"><span class="avatar" role="img" aria-label="Client portrait"></span><div><b>Elena Marsh</b><span>Private Client</span></div></div><h4>“You guys nailed it!”</h4><p>The team arranged every detail of our family plan with care. Every call was answered quickly and we always felt looked after. Truly a premium service.</p></div>
    <div class="card"><div class="card-head"><span class="avatar" role="img" aria-label="Client portrait"></span><div><b>Elena Marsh</b><span>Private Client</span></div></div><h4>“You guys nailed it!”</h4><p>The team arranged every detail of our family plan with care. Every call was answered quickly and we always felt looked after. Truly a premium service.</p></div>
    <div class="card"><div class="card-head"><span class="avatar" role="img" aria-label="Client portrait"></span><div><b>Elena Marsh</b><span>Private Client</span></div></div><h4>“You guys nailed it!”</h4><p>The team arranged every detail of our family plan with care. Every call was answered quickly and we always felt looked after. Truly a premium service.</p></div>
    <div class="card"><div class="card-head"><span class="avatar" role="img" aria-label="Client portrait"></span><div><b>Elena Marsh</b><span>Private Client</span></div></div><h4>“You guys nailed it!”</h4><p>The team arranged every detail of our family plan with care. Every call was answered quickly and we always felt looked after. Truly a premium service.</p></div>
    <div class="card"><div class="card-head"><span class="avatar" role="img" aria-label="Client portrait"></span><div><b>Elena Marsh</b><span>Private Client</span></div></div><h4>“You guys nailed it!”</h4><p>The team arranged every detail of our family plan with care. Every call was answered quickly and we always felt looked after. Truly a premium service.</p></div>
    <div class="card"><div class="card-head"><span class="avatar" role="img" aria-label="Client portrait"></span><div><b>Elena Marsh</b><span>Private Client</span></div></div><h4>“You guys nailed it!”</h4><p>The team arranged every detail of our family plan with care. Every call was answered quickly and we always felt looked after. Truly a premium service.</p></div>
  </div>
</section>

<section class="consult">
  <div class="consult-photo photo" role="img" aria-label="Doctor in a white coat seated on a chair"></div>
  <div class="consult-copy">
    <h2>Complimentary Consultation</h2>
    <div class="sub">Discover Your Path to Better Health</div>
    <p>Not sure where to begin? Schedule a free consultation with one of our experts to explore your options and tailor your journey to better health, with complete discretion.</p>
    <a class="btn">Schedule Your Free Consultation</a>
  </div>
</section>

<footer class="footer">
  <div class="brand"><span class="brand-mark"></span>Vantor Insurance<br>Services</div>
  <div class="fcol" style="left:420px"><h5>Company</h5>About Us<br>Our Team<br>Careers<br>Press</div>
  <div class="fcol" style="left:580px"><h5>Services</h5>Health Insurance<br>Concierge Medicine<br>Dental &amp; Vision<br>Enrollment</div>
  <div class="fcol" style="left:760px"><h5>Support</h5>Privacy Policy<br>Terms and Conditions<br>Client Portal<br>FAQ</div>
  <div class="fcol" style="left:940px"><h5>Contact</h5>(555) 010-2040<br>(555) 010-2041<br>(555) 010-2042<br>(555) 010-2043</div>
  <div class="copy">© 2025 Vantor Insurance Services. All Rights Reserved.</div>
</footer>

</body>
</html>
```